月経前症候群(PMS)に悩む女性向けにマニュアル配布をする
オプトLPのファーストビュー画像の制作(PC+スマホ)です。

- 案件名
美容LP(PMS訴求)のファーストビュー制作

- 目的
アドレス登録

- ターゲット
PMSに苦しんでいる20〜40代女性
特にイライラ、食欲増加、むくみ

- 制作範囲
スマホ・PC版のファーストビュー(CTAボタンまで)
CTA付近に、下のオファー内容をPCと書籍のモックアップで入れる

- コピー原稿+レイアウト参考
https://notes.paperlyn-share.net/document/d/7Qx2RbWm9KfTz3LpVn8YcH4sJd6UeA1oGi0NwMkZrXt/edit?usp=sharing

- コピー原稿
イライラ・食欲増加・むくみ
何をやってもよくならないPMSが良くなるマニュアル

- 強調ポイント
PMSが良くなる←下のURL1つ目の画像の「1年で結婚したい」のイメージ
マニュアル←「あなたのための婚活セミナー」
https://hanamori-zuan.jp/25/001-3/

- デザイン参考

- メイン画像:
PMSがよくなってにこやかな女性

- カラー
暖色系

- 納品
・透過PNG
(CTAエリアの入力フォームの前後で2つに分割して書き出していただきます)
・AI or PS, XD(元データ)
暖色系 ※どこかでこの色を使って欲しいです(#542D24)
コンペでは、スマホ版だけでオッケーです。当確後、PC版含めて納品いただければと思います。
モックアップの詳細の記載がないとのコメントをいただきましたが、コピー原稿に掲載があります。
それをPC画面と書籍の2パターンでご制作ください。

よろしくお願いいたします。

クオリティが高く、素敵なデザインだったので選ばせていただきました。
すごくセンスの良いデザイナーさんだと思いました。

とても悩んだので選ぶのに時間がかかってしまい
お待たせしてすみませんでした。
この度は素敵なデザインを本当にありがとうございました。

```html
<!DOCTYPE html>
<html lang="ja">
<head>
<meta charset="utf-8">
<title>PMSが良くなるマニュアル</title>
<link rel="stylesheet" href="https://fonts.googleapis.com/css2?family=Noto+Sans+JP:wght@400;700;900&family=Noto+Serif+JP:wght@500;700;900&display=swap">
<style>
:root{
  --pink:#e0508a;
  --pink-deep:#c73a74;
  --pink-soft:#f7d3e0;
  --blush:#fbeef2;
  --brown:#542D24;
  --ink:#3b2a2a;
  --white:#ffffff;
}
*{margin:0;padding:0;box-sizing:border-box}
html,body{width:799px;height:1200px;overflow:hidden;background:var(--white)}
body{font-family:"Noto Sans JP",sans-serif;color:var(--ink)}
.lp{position:relative;width:799px;height:1200px;overflow:hidden;background:linear-gradient(#fff 0,#fff 400px,var(--blush) 650px,#fff 1000px)}
.abs{position:absolute}
.topbar{left:0;top:0;width:799px;height:30px;background:linear-gradient(90deg,#f4b8cc,var(--pink),#f4b8cc);color:#fff;font:700 15px/30px "Noto Sans JP",sans-serif;text-align:center;letter-spacing:.05em}
.hero{left:0;top:30px;width:799px;height:370px;background:linear-gradient(90deg,#f3ddd5 0,#fbeff2 45%,#fff 70%)}
.hero-photo{left:40px;top:30px;width:380px;height:370px;background:radial-gradient(ellipse at 45% 40%,#e9c7b6,#d9a995 45%,#f5e3de 75%,transparent 76%)}
.author{left:10px;top:40px;font:700 15px/1.3 "Noto Serif JP",serif;color:var(--brown)}
.copy{left:400px;top:42px;width:390px;text-align:center;font-family:"Noto Serif JP",serif;white-space:nowrap}
.copy .pains{font-weight:900;font-size:28px;color:var(--pink-deep);letter-spacing:.02em}
.copy .sub{font-weight:700;font-size:20px;color:var(--brown);margin-top:4px}
.copy .main{font-weight:900;font-size:42px;color:var(--pink);line-height:1.15;margin-top:6px}
.copy .main small{font-size:30px;color:var(--brown)}
.copy .manual{font-weight:900;font-size:32px;color:var(--brown);line-height:1.2}
.copy .seminar{font-weight:900;font-size:30px;color:var(--pink);line-height:1.2;margin-top:4px}
.copy .seminar span{display:block;font-size:20px;color:var(--brown)}
.cta{display:flex;align-items:center;justify-content:center;border-radius:30px;background:linear-gradient(#ef7aa5,var(--pink-deep));color:#fff;font:900 24px/1 "Noto Sans JP",sans-serif;box-shadow:0 4px 0 #a22c5c;letter-spacing:.04em;white-space:nowrap}
.cta em{font-style:normal;color:#fff36b;font-size:28px}
.cta-hero{left:440px;top:300px;width:340px;height:48px}
.features{left:0;top:410px;width:799px;display:flex;justify-content:space-around;padding:0 20px}
.feature{width:210px;text-align:center}
.feature-photo{width:170px;height:170px;margin:0 auto;border-radius:50%;border:4px solid var(--pink-soft)}
.f1{background:linear-gradient(160deg,#f6e7e2,#d9c0b2)}
.f2{background:linear-gradient(160deg,#f1d6de,#c9a0ae)}
.f3{background:linear-gradient(160deg,#e7d2b6,#b58a58)}
.feature p{margin-top:8px;font:700 16px/1.35 "Noto Sans JP",sans-serif;color:var(--brown)}
.lines{left:0;top:650px}
.bubble{width:84px;height:84px;border-radius:50%;background:#fff;border:3px solid var(--pink);display:flex;align-items:center;justify-content:center;text-align:center;font:900 22px/1.1 "Noto Serif JP",serif;color:var(--brown);z-index:2;white-space:nowrap}
.bubble b{color:var(--pink);font-size:30px}
.box{background:#fff;border:2px solid var(--brown);font:400 15px/1.4 "Noto Sans JP",sans-serif;padding:14px 14px 14px 40px;color:var(--ink)}
.b-top{left:325px;top:690px;width:220px;height:115px}
.b-left{left:60px;top:820px;width:230px;height:115px}
.b-right{left:540px;top:820px;width:230px;height:115px}
.q-top{left:265px;top:660px}
.q-left{left:10px;top:790px;font-size:17px}
.q-right{left:480px;top:790px}
.center-copy{left:250px;top:935px;width:300px;text-align:center;font:900 22px/1.2 "Noto Serif JP",serif;color:var(--pink)}
.center-copy span{color:var(--brown);display:block}
.bottom{left:0;top:1005px;width:799px;height:195px;background:linear-gradient(90deg,#f4ddd2,#fdf3f0 40%,#fff)}
.bottom-photo{left:20px;top:1005px;width:220px;height:195px;background:linear-gradient(160deg,#ecd0c1,#c99a86)}
.book{left:650px;top:1030px;width:120px;height:85px;background:linear-gradient(135deg,#f6e4e6,#d7b7bc);border:1px solid #e6cdd2}
.bottom-copy{left:245px;top:1020px;width:400px;text-align:center;font-family:"Noto Serif JP",serif;color:var(--brown);white-space:nowrap}
.bottom-copy .l1{font-weight:900;font-size:18px;line-height:1.35}
.bottom-copy .l1 em{font-style:normal;color:var(--pink)}
.bottom-copy .l2{font-weight:900;font-size:23px;line-height:1.3;color:var(--pink-deep);margin-top:6px}
.cta-bottom{left:250px;top:1128px;width:380px;height:52px}
</style>
</head>
<body>
<main class="lp">
  <div class="abs topbar">アプローチが下手でも1年以内に結婚したいあなたへ</div>
  <div class="abs hero"></div>
  <div class="abs hero-photo" role="img" aria-label="PMSが良くなって明るく微笑む女性の写真"></div>
  <p class="abs author">美容家<br>花村 涼子 著</p>

  <div class="abs copy">
    <p class="pains">イライラ・食欲増加・むくみ</p>
    <p class="sub">何をやってもよくならない</p>
    <p class="main">PMS<small>が</small>良くなる</p>
    <p class="manual">マニュアル</p>
    <p class="seminar">1年で結婚したい<span>あなたのための婚活セミナー</span></p>
  </div>
  <a class="abs cta cta-hero">今すぐ<em>無料</em>で手に入れる</a>

  <section class="abs features">
    <div class="feature"><div class="feature-photo f1" role="img" aria-label="穏やかに過ごす女性の写真"></div><p>陰陽五行的<br>体質改善</p></div>
    <div class="feature"><div class="feature-photo f2" role="img" aria-label="肌の手入れをする女性の写真"></div><p>肌も身体も<br>きれいになる方法</p></div>
    <div class="feature"><div class="feature-photo f3" role="img" aria-label="薬膳の食材の写真"></div><p>忙しい女子でも<br>手軽にできるゆる薬膳</p></div>
  </section>

  <svg class="abs lines" width="799" height="300" viewBox="0 0 799 300" aria-hidden="true">
    <path d="M435 155 L435 190 M175 170 L175 150 L640 150 L640 170" fill="none" stroke="var(--pink)" stroke-width="2"/>
  </svg>

  <div class="abs bubble q-top"><span><b>食</b>欲<br>増加</span></div>
  <div class="abs box b-top">アドバイス text</div>
  <div class="abs bubble q-left"><span>イライラ</span></div>
  <div class="abs box b-left">イライラとは?とアドバイス</div>
  <div class="abs bubble q-right"><span><b>む</b>くみ</span></div>
  <div class="abs box b-right">アドバイス text</div>

  <p class="abs center-copy">PMSが良くなるマニュアル<span>1年で結婚したい</span></p>

  <div class="abs bottom"></div>
  <div class="abs bottom-photo" role="img" aria-label="微笑む美容家の写真"></div>
  <div class="abs book" role="img" aria-label="マニュアル書籍のモックアップ"></div>
  <div class="abs bottom-copy">
    <p class="l1">3万人見てきた美容家が<br>こっそり教える<em>“本当に正しい美容法”</em>とは?</p>
    <p class="l2">間違いだらけのスキンケアの常識</p>
  </div>
  <a class="abs cta cta-bottom">今すぐ<em>無料</em>で手に入れる</a>
</main>
</body>
</html>
```